Tindale Reach Face Cleanser Labels

We need a label design for a soon to launch company in Charlotte, NC, called Tindale Reach. We are in the health & beauty business and our focus is on product purity. We use only organic ingredients that are pure, fresh and clean. We have just finished the design work on the logo and would like to see who can come up with a label design that could work across the board on several of our products. We are aiming to have complete continuity between labels. They need to be classy, reflect a national brand and be legible and easily reproducible, as well as easily branded.

The first label we would like to start with will be for our product called, "Facial Cleanser". It comes in 2 different sizes: 2 oz., and 4 oz. The labels will wrap around a low profile jar about 1" wide and 7" long.

The copy needs to be in black or dark grey, while the tree in the logo can be a variation of orange. Our color is orange and aqua and can be added if desired.

The label will include the product name, company logo (including slogan), size, directions, ingredients, mfr. address and say Made in the USA, etc. (see below).

We are ultimately looking for a design that we could use to brand all of our products with. We would simply like this project as the template/basis for all of our labels. Consequently, we will need the details of your design (fonts used, etc.) once complete and paid for.

Here is what is included on the label:
product name: Quillara (Daily) Face Cleanser - can be simply, "Facial Cleanser" or both
recycle sign
made in the USA
size: 2 oz./59 ml; 4 oz./118 ml
address: PO Box 718, Fenmore, NC 28390
website scan code
Ingredients: Sodium bicarbonate, organic extra virgin olive oil, organic virgin coconut oil, sweet almond oil, organic virgin jojoba oil, honey, vitamin E oil, proprietary blend of
therapeutic essential oils.
Directions: Splash face with warm water. Take a pea sized dab and rub into palms and fingers to coat. Then apply to entire face, avoiding eye area. Scrub gently using fingers and palms. Rinse thoroughly with warm water. Dab dry with cotton towel. Stir as needed.
Updates

We have added required content to the label. We like what we see so far but would like to see some more submissions before making our final call. Thank you for all of your submissions so far!

Target Market(s)

Health conscious individuals who prefer pure, organic and wholesome products.

Industry/Entity Type

Health

Colors
faa54b

Requirements
Must have
• Logo needs to stand out and be easily branded. Needs to be elegant and classy.

```html
<!DOCTYPE html>
<html lang="en">
<head>
<meta charset="utf-8">
<title>Tindale Reach – Quillara Daily Face Cleanser Label</title>
<link href="https://fonts.googleapis.com/css2?family=Archivo+Black&family=Tinos:wght@400;700&display=swap" rel="stylesheet">
<style>
  :root {
    --bg: #f4f4f2;
    --label: #ffffff;
    --ring: #fbb817;
    --brand: #e9861c;
    --sun: #f7b500;
    --aqua-bar: #5aa9d9;
    --gold-bar: #e6a11f;
    --ink: #1b1b1b;
    --ink-soft: #333333;
    --edge: #d9d9d6;
  }
  * { box-sizing: border-box; margin: 0; padding: 0; }
  html, body { width: 1200px; height: 774px; overflow: hidden; }
  body {
    background: var(--bg);
    font-family: "Tinos", "Times New Roman", serif;
    color: var(--ink);
    position: relative;
  }

  /* Lid label */
  .lid-label {
    position: absolute;
    left: 350px; top: 24px;
    width: 500px; height: 500px;
    border-radius: 50%;
    background: var(--label);
    border: 1px solid var(--edge);
    display: flex; align-items: center; justify-content: center;
  }
  .lid-ring {
    width: 456px; height: 456px;
    border-radius: 50%;
    border: 3px solid var(--ring);
    display: flex; flex-direction: column; align-items: center;
    padding-top: 88px;
  }
  .brand-name {
    font-family: "Tinos", "Times New Roman", serif;
    font-weight: 700;
    color: var(--brand);
    font-size: 40px;
    line-height: 1.1;
    text-align: center;
  }
  .product-title {
    font-family: "Archivo Black", "Arial Black", sans-serif;
    font-size: 36px;
    letter-spacing: 0.5px;
    margin-top: 34px;
    text-transform: uppercase;
  }
  .product-bar {
    font-family: "Archivo Black", "Arial Black", sans-serif;
    color: #fff;
    background: var(--aqua-bar);
    font-size: 25px;
    padding: 2px 22px;
    letter-spacing: 0.5px;
    text-transform: uppercase;
    margin-top: 4px;
  }
  .sun-mark {
    width: 78px; height: 78px;
    border-radius: 50%;
    background: var(--sun);
    margin-top: 26px;
  }
  .size {
    font-size: 18px;
    margin-top: 22px;
    letter-spacing: 0.5px;
  }

  /* Wrap-around side label */
  .wrap-label {
    position: absolute;
    left: 40px; top: 570px;
    width: 1120px; height: 170px;
    background: var(--label);
    border: 1px solid var(--edge);
    display: grid;
    grid-template-columns: 1fr 420px 1fr;
    align-items: center;
    padding: 0 36px;
    gap: 34px;
  }
  .panel-text {
    font-size: 13.5px;
    line-height: 1.35;
    color: var(--ink-soft);
  }
  .panel-text strong { color: var(--ink); }
  .panel-text .origin { margin-top: 8px; }
  .wrap-center {
    display: flex; flex-direction: column; align-items: center;
  }
  .wrap-title {
    font-family: "Archivo Black", "Arial Black", sans-serif;
    font-size: 31px;
    text-transform: uppercase;
  }
  .wrap-bar {
    font-family: "Archivo Black", "Arial Black", sans-serif;
    color: #fff;
    background: var(--gold-bar);
    font-size: 22px;
    padding: 2px 40px;
    text-transform: uppercase;
    margin-top: 4px;
  }
  .wrap-size { font-size: 18px; margin-top: 12px; }
</style>
</head>
<body>
  <section class="lid-label">
    <div class="lid-ring">
      <div class="brand-name">Tindale Reach</div>
      <div class="product-title">Quillara Daily</div>
      <div class="product-bar">Face Cleanser</div>
      <div class="sun-mark" role="img" aria-label="Yellow sun flower emblem"></div>
      <div class="size">4 OZ./118 ML</div>
    </div>
  </section>

  <section class="wrap-label">
    <div class="panel-text">
      <p><strong>Ingredients:</strong> Sodium bicarbonate, organic extra virgin olive oil, organic virgin coconut oil, sweet almond oil, organic virgin jojoba oil, honey, vitamin E oil, proprietary blend of therapeutic essential oils.</p>
      <p class="origin">PO Box 718, Fenmore, NC 28390 · Made in the USA</p>
    </div>
    <div class="wrap-center">
      <div class="wrap-title">Quillara Daily</div>
      <div class="wrap-bar">Face Cleanser</div>
      <div class="wrap-size">4 OZ./118 ML</div>
    </div>
    <div class="panel-text">
      <p><strong>Directions:</strong> Splash face with warm water. Take a pea sized dab and rub into palms and fingers to coat. Then apply to entire face, avoiding eye area. Scrub gently using fingers and palms. Rinse thoroughly with warm water. Dab dry with cotton towel. Stir as needed.</p>
    </div>
  </section>
</body>
</html>
```